Rise As Captain Book Cover Design

Book Cover Design Brief
Book Title
Rise As Captain
Subtitle
The 10 Quiet Habits of Remarkable Command
Author
Orwen Dalquist
Overview
This book is about leadership that starts within.
Most leadership books focus on tactics or management strategies. This book focuses on the inner disciplines that create powerful leaders — mindset, integrity, focus, empathy, professionalism, honesty, and self-respect.
The tone of the book is bold, direct, confident, and transformational.
This is not a soft or corporate leadership book. It is a call to step up and become the leader you are capable of becoming.
The cover should feel:
• Powerful
• Professional
• Transformational
• Premium
• Memorable
Think best-selling leadership book, not a generic business book.
Target Audience
Business owners
Managers
Entrepreneurs
Team leaders
Professionals who want to grow as leaders
Most readers are ambitious professionals who want to level up their leadership and life.
Design Direction
The design should communicate:
Strength. Discipline. Leadership. Personal transformation.
Avoid cliché leadership visuals like:
• Handshakes
• Office buildings
• Corporate stock imagery
• Teams sitting around tables
The design should feel iconic, bold, and timeless.
Think about covers of successful leadership books such as:
Copper Rituals
Total Stewardship
Won't Break Now
Begin From Purpose
The 36 Rules of Sway
These covers are simple, powerful, and recognizable even at small sizes.
Typography
The title RISE AS CAPTAIN should be:
• Bold
• Strong
• Dominant on the cover
• Easy to read even at small sizes (important for Vellora thumbnails)
The subtitle should be clean and secondary to the title.
The overall typography should feel strong, modern, and premium.
Color Direction
Designers are free to explore colors, but the cover should feel strong and premium, not playful.
Colors that often work well for leadership books include:
Black
Gold
White
Deep blue
Dark red
High contrast and clarity are important.
Style
Preferred style:
• Clean
• Modern
• Minimal
• Strong contrast
Avoid clutter and overly busy designs.
The goal is to create a cover that feels powerful and professional at first glance.
Deliverables
Front cover design for a leadership book.
Final files should include:
• High resolution artwork
• Editable source files
• Print-ready version suitable for publishing
Goal of the Cover
When someone sees this book on Vellora or in a bookstore, they should immediately think:
“This looks like a serious leadership book.”
The design should feel like it belongs next to books by authors such as:
Marcus Thorley
Brandt Osgood
Peter Hollis
Nolan Fairbrook
A strong, confident cover that attracts leaders who want to grow and perform at a higher level.
Target Market(s)
Business Owners and High level managers
Look and feel
Each slider illustrates characteristics of the customer's brand and the style your logo design should communicate.

```html
<!DOCTYPE html>
<html lang="en">
<head>
<meta charset="utf-8">
<title>Rise As Captain — Book Cover</title>
<link rel="stylesheet" href="https://fonts.googleapis.com/css2?family=Montserrat:wght@500;800&family=Oswald:wght@600&display=swap">
<style>
  :root {
    --backdrop: #e2e2e2;
    --red-light: #d8333c;
    --red: #cf1426;
    --red-deep: #c10f20;
    --ink: #070707;
    --paper: #ffffff;
    --glow-red: rgba(207, 20, 38, 0);
    --glow-light: #f1dcde;
  }
  * { margin: 0; padding: 0; box-sizing: border-box; }
  html, body {
    width: 1200px;
    height: 933px;
    overflow: hidden;
    background: var(--backdrop);
  }
  .cover {
    position: absolute;
    left: 344px;
    top: 92px;
    width: 486px;
    height: 722px;
    background: linear-gradient(120deg, var(--red-light) 0%, var(--red) 40%, var(--red-deep) 100%);
    overflow: hidden;
  }
  .author {
    position: absolute;
    top: 50px;
    left: 0;
    width: 100%;
    text-align: center;
    font-family: "Montserrat", sans-serif;
    font-weight: 500;
    font-size: 29px;
    letter-spacing: 4px;
    color: var(--paper);
  }
  .doorway-art {
    position: absolute;
    left: 36px;
    top: 282px;
    width: 380px;
    height: 260px;
    background: linear-gradient(160deg, var(--glow-red) 0%, var(--glow-red) 35%, var(--glow-light) 100%);
  }
  .title {
    font-family: "Oswald", sans-serif;
    font-weight: 600;
    color: var(--paper);
    text-transform: uppercase;
  }
  .title-line {
    position: absolute;
    display: block;
    line-height: 1;
    white-space: nowrap;
    font-size: 104px;
  }
  .title-line--top {
    top: 170px;
    left: 0;
    width: 100%;
    text-align: center;
  }
  .title-line--main {
    top: 280px;
    left: 72px;
    letter-spacing: -1px;
  }
  .subtitle-band {
    position: absolute;
    left: 0;
    top: 542px;
    width: 100%;
    height: 180px;
    background: var(--ink);
    display: flex;
    align-items: center;
    justify-content: center;
  }
  .subtitle {
    font-family: "Montserrat", sans-serif;
    font-weight: 800;
    font-size: 22px;
    line-height: 1.4;
    text-align: center;
    text-transform: uppercase;
    color: var(--paper);
  }
</style>
</head>
<body>
  <main class="cover">
    <p class="author">ORWEN DALQUIST</p>

    <div class="doorway-art" role="img" aria-label="Illustration: a lit open doorway with a lone figure stepping out, light spilling forward as a widening path"></div>

    <h1 class="title">
      <span class="title-line title-line--top">Rise As</span>
      <span class="title-line title-line--main">Captain</span>
    </h1>

    <div class="subtitle-band">
      <p class="subtitle">The 10 Quiet Habits of<br>Remarkable Command</p>
    </div>
  </main>
</body>
</html>
```